New Business Card Design Project VORASTI-Italy

we are VORASTI-Italy
our company in the market for 3 years we are luxury cosmetic company and its about time for a facelift :)
i will like to have elegant luxurious and unique business card
that will give the person that get it a unique, luxurious and elegant impression
I'm VERY OPEN FOR NEW IDEAS , even duo i add a few files of things that i see on line and i like them

i add my logo as well
my website is VORASTI.COM
(if you would like to see the main style that we have)

Target Market(s)

adult that have money :)

Industry/Entity Type

Business

Contact Information for Business Card

Name - Paul Vorasti
Position - CEO and CO Founder
address - 4817 E Larkdale
telephone - 555-384-1962
email - paul@vorasti.com
fax - 555-384-1962
website - VORASTI.COM

Colors
000000
959595
fbee3e
ffffff

Requirements
Must have
• big logo in GOLD color
• elegant look
• impressive
Nice to have
• not must but maybe classy pattern background
• not must but maybe emblem
• maybe clear plastic business card
Should not have
• colors
• images

```html
<!DOCTYPE html>
<html lang="en">
<head>
<meta charset="utf-8">
<title>VORASTI Italy – Business Card</title>
<link rel="stylesheet" href="https://fonts.googleapis.com/css2?family=Cinzel:wght@400;500&family=Roboto:wght@400&display=swap">
<style>
  :root {
    --ink: #0b0d0d;
    --gold: #d2b22c;
    --gold-light: #f1e04a;
    --gold-deep: #c9a623;
    --paper: #ffffff;
    --text: #333638;
    --ghost: #ececec;
  }
  * { margin: 0; padding: 0; box-sizing: border-box; }
  html, body { width: 1200px; height: 720px; overflow: hidden; background: var(--paper); }
  .card { position: relative; width: 1200px; height: 720px; overflow: hidden; background: var(--paper); }

  .brand-panel {
    position: absolute; left: 0; top: 0; width: 594px; height: 720px;
    background: var(--ink);
  }
  .brand-circle {
    position: absolute; left: 214px; top: 158px; width: 206px; height: 206px;
    border: 5px solid var(--gold); border-radius: 50%;
  }
  .brand-name {
    position: absolute; left: 0; width: 594px; text-align: center;
    font-family: "Cinzel", serif; font-weight: 400; color: var(--gold);
  }
  .brand-name--main { top: 415px; font-size: 84px; letter-spacing: 1px; line-height: 1; }
  .brand-rule {
    position: absolute; left: 91px; top: 512px; width: 453px; height: 4px;
    background: var(--gold);
  }
  .brand-name--sub { top: 537px; font-size: 31px; letter-spacing: 3px; line-height: 1; }

  .gold-strip {
    position: absolute; left: 594px; top: 0; width: 11px; height: 720px;
    background: linear-gradient(180deg, var(--gold-deep), var(--gold-light) 25%, var(--gold) 60%, var(--gold-deep));
  }

  .ghost-circle {
    position: absolute; left: 860px; top: -120px; width: 560px; height: 560px;
    border: 28px solid var(--ghost); border-radius: 50%; opacity: 0.7;
  }

  .person { position: absolute; left: 661px; top: 177px; }
  .person__name {
    font-family: "Cinzel", serif; font-weight: 500; font-size: 48px;
    color: var(--gold); letter-spacing: 2px; line-height: 1;
  }
  .person__role {
    margin-top: -2px; font-family: "Roboto", sans-serif; font-size: 28px; color: var(--text);
  }

  .contacts { position: absolute; left: 666px; top: 338px; list-style: none; }
  .contacts__item {
    display: flex; align-items: flex-start; gap: 16px;
    font-family: "Roboto", sans-serif; font-size: 27px; line-height: 36px; color: var(--text);
    margin-bottom: 10px;
  }
  .contacts__icon { width: 26px; height: 26px; margin-top: 5px; flex: none; }
  .contacts__icon path, .contacts__icon circle, .contacts__icon rect, .contacts__icon ellipse, .contacts__icon line {
    fill: none; stroke: var(--gold); stroke-width: 1.6;
  }
  .contacts__icon .solid { fill: var(--gold); stroke: none; }
</style>
</head>
<body>
<main class="card">
  <section class="brand-panel">
    <div class="brand-circle"></div>
    <div class="brand-name brand-name--main">VORASTI</div>
    <div class="brand-rule"></div>
    <div class="brand-name brand-name--sub">ITALY</div>
  </section>

  <div class="gold-strip"></div>
  <div class="ghost-circle"></div>

  <section class="person">
    <h1 class="person__name">PAUL VORASTI</h1>
    <p class="person__role">CEO and CO Founder</p>
  </section>

  <ul class="contacts">
    <li class="contacts__item">
      <svg class="contacts__icon" viewBox="0 0 26 26" aria-hidden="true">
        <path d="M6 3 L10 8 L8 11 C9.5 14 12 16.5 15 18 L18 16 L23 20 L20 23 C12 23 3 14 3 6 Z"/>
      </svg>
      <span>(555)-384-1962</span>
    </li>
    <li class="contacts__item">
      <svg class="contacts__icon" viewBox="0 0 26 26" aria-hidden="true">
        <rect x="2" y="6" width="22" height="15"/>
        <path d="M2 6 L13 15 L24 6 M2 21 L10 13 M24 21 L16 13"/>
      </svg>
      <span>paul@vorasti.com</span>
    </li>
    <li class="contacts__item">
      <svg class="contacts__icon" viewBox="0 0 26 26" aria-hidden="true">
        <circle cx="13" cy="13" r="10.5"/>
        <ellipse cx="13" cy="13" rx="4.5" ry="10.5"/>
        <line x1="2.5" y1="13" x2="23.5" y2="13"/>
        <path d="M4.5 7.5 H21.5 M4.5 18.5 H21.5"/>
      </svg>
      <span>VORASTI.COM</span>
    </li>
    <li class="contacts__item">
      <svg class="contacts__icon" viewBox="0 0 26 26" aria-hidden="true">
        <path class="solid" d="M13 1 C8 1 5 5 5 9 C5 15 13 25 13 25 C13 25 21 15 21 9 C21 5 18 1 13 1 Z M13 6 A3.2 3.2 0 1 0 13.01 6 Z"/>
      </svg>
      <span>4817 E Larkdale Ave<br>Brookfield N.V 20931</span>
    </li>
  </ul>
</main>
</body>
</html>
```